CPA Graduation Party

I need to make simple invitation for my sister's recent success, passing the CPA (Certified Public Accountant) exam. It is a surprise party. I want very simple and professional looking invitation. My only requirements are that you don't use any graduation caps or gowns due to the fact that it's not an actual graduation. It's a series of exams that she passes. Be creative with the design but once again, keep it professional. I have attached a font called iScriptSTD. I liked the font so was thinking about using it. But it's not necessary. If you have something slimier or better, please use it.

I was planning on printing on a specific kind of paper. It's called pearlized ivory cardstock. It has a little coating and shine on it and since it's ivory, I was thinking about the main color of the invitation to be burgundy type. For example, see the following RGB: R204, G0, B102.

Party info:
Name: Ravita
Date & Time: Saturday, March 8th, 2014 at 6:00pm
Location: Tirel Hall. 418 Wexmoor Lane Parsippany, NJ 07381

I know I didn't provide a lot of info for the invite but please be creative.  Use general knowledge and other formal party invites as examples. I am not looking for a name, date and location as three bullets on the card.

Also, I forgot to mention the size of the invite.  It should be 5.5x8.5.  Thank you.

Requirements
Should not have
• graduation caps and/or gowns

```html
<!DOCTYPE html>
<html lang="en">
<head>
<meta charset="utf-8">
<title>Surprise Party Invitation – Ravita</title>
<link rel="stylesheet" href="https://fonts.googleapis.com/css2?family=Caveat+Brush&display=swap">
<style>
  :root {
    --page: #fdfdfd;
    --card: #f0f0f0;
    --ribbon: #cc0066;
    --band: #aa0066;
    --fold: #770044;
    --ink: #cc0066;
    --light: #ffffff;
  }
  * { margin: 0; padding: 0; box-sizing: border-box; }
  html, body {
    width: 1200px; height: 1000px; overflow: hidden;
    background: var(--page);
    font-family: "Caveat Brush", cursive;
  }
  .invitation {
    position: absolute; left: 118px; top: 178px;
    width: 971px; height: 628px;
    background: var(--card);
  }
  .ornaments { position: absolute; left: 0; top: 0; width: 971px; height: 628px; }
  .line {
    position: absolute; left: 0; width: 100%;
    text-align: center; color: var(--ink); white-space: nowrap;
  }
  .title-banner { top: 50px; font-size: 28px; color: var(--light); letter-spacing: 0.5px; }
  .for { top: 100px; font-size: 28px; }
  .guest-name { top: 128px; font-size: 86px; line-height: 1; letter-spacing: 2px; }
  .occasion { top: 222px; font-size: 26px; }
  .label { font-size: 18px; color: var(--light); }
  .label-on { top: 287px; }
  .label-at { top: 391px; }
  .date { top: 338px; font-size: 28px; }
  .venue { top: 444px; font-size: 28px; }
  .rsvp { top: 522px; font-size: 22px; color: var(--light); }
</style>
</head>
<body>
  <main class="invitation">
    <svg class="ornaments" viewBox="0 0 971 628" aria-hidden="true">
      <!-- top band and title ribbon -->
      <rect x="0" y="64" width="971" height="43" fill="var(--band)"/>
      <polygon points="349,90 406,90 406,107" fill="var(--fold)"/>
      <polygon points="582,90 639,90 582,107" fill="var(--fold)"/>
      <rect x="349" y="47" width="290" height="43" fill="var(--ribbon)"/>

      <!-- "On" ribbon -->
      <polygon points="434,294 464,294 464,320 434,320 448,307" fill="var(--band)"/>
      <polygon points="532,294 562,294 548,307 562,320 532,320" fill="var(--band)"/>
      <polygon points="464,312 484,312 484,320 464,320" fill="var(--fold)"/>
      <polygon points="512,312 532,312 532,320 512,320" fill="var(--fold)"/>
      <rect x="464" y="284" width="68" height="28" fill="var(--ribbon)"/>

      <!-- "At" ribbon -->
      <polygon points="434,398 464,398 464,424 434,424 448,411" fill="var(--band)"/>
      <polygon points="532,398 562,398 548,411 562,424 532,424" fill="var(--band)"/>
      <polygon points="464,416 484,416 484,424 464,424" fill="var(--fold)"/>
      <polygon points="512,416 532,416 532,424 512,424" fill="var(--fold)"/>
      <rect x="464" y="388" width="68" height="28" fill="var(--ribbon)"/>

      <!-- bottom band and RSVP ribbon -->
      <rect x="0" y="532" width="971" height="43" fill="var(--band)"/>
      <polygon points="170,558 226,558 226,575" fill="var(--fold)"/>
      <polygon points="761,558 817,558 761,575" fill="var(--fold)"/>
      <rect x="170" y="515" width="647" height="43" fill="var(--ribbon)"/>
    </svg>

    <p class="line title-banner">Surprise Party</p>
    <p class="line for">For</p>
    <h1 class="line guest-name">RAVITA</h1>
    <p class="line occasion">to celebrate her passing the CPA exam</p>
    <p class="line label label-on">On</p>
    <p class="line date">Saturday, March 8th, 2014 at 6.00 pm</p>
    <p class="line label label-at">At</p>
    <p class="line venue">Tirel Hall. 418 Wexmoor Lane Parsippany, NJ 07381</p>
    <p class="line rsvp">RSVP at kdesai2286@inboxmail.com or call (555) 318 - 2047</p>
  </main>
</body>
</html>
```